Tozvar new design for business cards we want to change our existing design. Logo must remain the same

Hello we are the company TozVar and offer various services regarding transportation and disposal. In addition to our main acquisition of van rental, we also offer disposal and express transportation, so we need new business card designs for our business. Our elders have their time and do not like it anymore. We want to change our existing design. Logo must remain the same as well as the color blue, whether dark or light Does not play a big role in the best medium blue. Logo must be present on the front side. As well as telephone, email, web and location. Big enough but not too big. Back can be redesigned Logo as well as name TozVar must be present. Important is the text: Van rental Disposal and clearing express transportation. Without bail in red should be noted somewhere. it should be modern but not too playful. rather serious but no beating company Thank you very much

Target Market(s)

Private customers as well as companies we want to change our existing design. Logo must remain the same as well as the color blue, whether dark or light Does not play a big role in the best medium blue. Logo must be present on the front side. As well as telephone, email, web and location. Big enough but not too big. Back can be redesigned Logo as well as name TozVar must be present. Important is the text: Van rental Disposal and clearing express transportation. Without bail in red should be noted somewhere. it should be modern but not too playful. rather serious but no beating company Thank you very much

Industry/Entity Type

Car Rental

Contact Information for Business Card

we want to change our existing design. Logo must remain the same as well as the color blue, whether dark or light Does not play a big role in the best medium blue.
Logo must be present on the front side.
As well as telephone, email, web and location. Big enough but not too big.
Back can be redesigned Logo as well as name TozVar must be present.
Important is the text:
Van rental
Disposal and clearing
Express transportation.
Without bail in red should be noted somewhere.
it should be modern but not too playful. rather serious but no beating company
Thank you very much

Font styles to use
Sans Serif

Colors
33a6d7
ec1f27
0692cd
3277b5

Requirements
Must have
• logo and name TozVar as described in the above text must have it. we want to change our existing design. Logo must remain the same as well as the color blue, whether dark or light Does not play a big role in the best medium blue. Logo must be present on the front side. As well as telephone, email, web and location. Big enough but not too big. Back can be redesigned Logo as well as name TozVar must be present. Important is the text: Van rental Disposal and clearing express transportation. Without bail in red should be noted somewhere. it should be modern but not too playful. rather serious but no beating company Thank you very much
Nice to have
• see description we want to change our existing design. Logo must remain the same as well as the color blue, whether dark or light Does not play a big role in the best medium blue. Logo must be present on the front side. As well as telephone, email, web and location. Big enough but not too big. Back can be redesigned Logo as well as name TozVar must be present. Important is the text: Van rental Disposal and clearing express transportation. Without bail in red should be noted somewhere. it should be modern but not too playful. rather serious but no beating company Thank you very much
Should not have
• Blue White and little red we want to change our existing design. Logo must remain the same as well as the color blue, whether dark or light Does not play a big role in the best medium blue. Logo must be present on the front side. As well as telephone, email, web and location. Big enough but not too big. Back can be redesigned Logo as well as name TozVar must be present. Important is the text: Van rental Disposal and clearing express transportation. Without bail in red should be noted somewhere. it should be modern but not too playful. rather serious but no beating company Thank you very much

```html
<!DOCTYPE html>
<html lang="de">
<head>
<meta charset="utf-8">
<title>TozVar GmbH – Business Cards</title>
<link href="https://fonts.googleapis.com/css2?family=Montserrat:wght@500;600;700&display=swap" rel="stylesheet">
<style>
  :root{
    --stage:#dcdddf;
    --card:#ffffff;
    --navy:#0a0f72;
    --slate:#7f9ab6;
    --steel:#4e6699;
    --shadow:rgba(0,0,0,.16);
  }
  *{margin:0;padding:0;box-sizing:border-box}
  html,body{width:1200px;height:900px;overflow:hidden;background:var(--stage)}
  body{font-family:"Montserrat",Arial,sans-serif;position:relative}
  .card{position:absolute;width:514px;height:297px;background:var(--card);box-shadow:2px 4px 6px var(--shadow);overflow:hidden}
  .card--tagline{left:73px;top:138px}
  .card--contact-a{left:615px;top:138px}
  .card--address{left:73px;top:464px}
  .card--contact-b{left:615px;top:464px}

  .brand{position:absolute;color:var(--navy);font-weight:700;letter-spacing:.5px;white-space:nowrap;line-height:1}
  .brand--small{left:245px;top:62px;font-size:30px}
  .brand--large{font-size:44px}
  .card--contact-a .brand--large{left:40px;top:128px}
  .card--address .brand--large{left:318px;top:72px;font-size:38px}
  .card--contact-b .brand--large{left:36px;top:128px;font-size:42px}

  .services{position:absolute;left:40px;top:182px;color:var(--slate);font-weight:600;font-size:21px;line-height:24px;text-transform:uppercase}
  .services__note{font-size:11px;line-height:14px;font-weight:600;margin-top:2px}

  .contacts{position:absolute;list-style:none;color:var(--slate);font-weight:600;font-size:21px;line-height:29px}
  .contacts li{display:flex;align-items:center;gap:7px}
  .contacts svg{width:16px;height:16px;flex:none}
  .card--contact-a .contacts{left:251px;top:112px}
  .card--address .contacts{left:80px;top:192px}
  .card--contact-b .contacts{left:199px;top:122px}

  .address-line{position:absolute;color:var(--slate);font-weight:600;font-size:13.5px;letter-spacing:.2px;white-space:nowrap}
  .card--contact-a .address-line{left:100px;top:265px}
  .card--contact-b .address-line{left:62px;top:276px}

  .address-block{position:absolute;left:80px;top:37px;color:var(--slate);font-size:14px;line-height:16px;font-weight:500}
  .address-block strong{font-weight:700}

  .side-band{position:absolute;left:0;top:0;width:53px;height:100%;background:var(--slate)}
  .arrow-panel{position:absolute;right:0;top:0;width:72px;height:100%}
</style>
</head>
<body>
<svg width="0" height="0" style="position:absolute" aria-hidden="true">
  <defs>
    <symbol id="icon-phone" viewBox="0 0 16 16"><rect x="1" y="1" width="14" height="14" rx="4" fill="none" stroke="currentColor" stroke-width="1.4"/><path d="M4.5 9.5c0-2 1.6-3 3.5-3s3.5 1 3.5 3H9.8V8.4H6.2v1.1z" fill="currentColor"/></symbol>
    <symbol id="icon-mail" viewBox="0 0 16 16"><rect x="1" y="1" width="14" height="14" rx="4" fill="none" stroke="currentColor" stroke-width="1.4"/><rect x="4" y="5" width="8" height="6" rx="1" fill="currentColor"/><path d="M4.3 5.5 8 8.3l3.7-2.8" fill="none" stroke="#fff" stroke-width="1"/></symbol>
    <symbol id="icon-web" viewBox="0 0 16 16"><rect x="1" y="1" width="14" height="14" rx="4" fill="none" stroke="currentColor" stroke-width="1.4"/><circle cx="8" cy="8" r="3.6" fill="none" stroke="currentColor" stroke-width="1"/><path d="M4.4 8h7.2M8 4.4v7.2M6.3 4.8c-1 2-1 4.4 0 6.4M9.7 4.8c1 2 1 4.4 0 6.4" fill="none" stroke="currentColor" stroke-width=".8"/></symbol>
  </defs>
</svg>

<section class="card card--tagline">
  <div class="brand brand--small">TOZVAR GMBH</div>
  <div class="services">
    <p>Van Rental</p>
    <p>Disposal and Clearing</p>
    <p>Express Transportation</p>
    <p class="services__note">Without bail in red</p>
  </div>
</section>

<section class="card card--contact-a">
  <div class="brand brand--large">TozVar</div>
  <ul class="contacts">
    <li><svg><use href="#icon-phone"/></svg>+41 (71) 402 55 18</li>
    <li><svg><use href="#icon-mail"/></svg>INFO@TOZVAR.CH</li>
    <li><svg><use href="#icon-web"/></svg>WWW.TOZVAR.CH</li>
  </ul>
  <p class="address-line">WERKHOFWEG 7, 9405 SEEBRUNN, OSTGAU</p>
</section>

<section class="card card--address">
  <div class="side-band"></div>
  <div class="address-block">
    <strong>TozVar GmbH</strong><br>
    Werkhofweg 7<br>
    9405 Seebrunn, Ostgau
  </div>
  <div class="brand brand--large">TozVar</div>
  <ul class="contacts">
    <li><svg><use href="#icon-phone"/></svg>+41 (71) 402 55 18</li>
    <li><svg><use href="#icon-mail"/></svg>INFO@TOZVAR.CH</li>
    <li><svg><use href="#icon-web"/></svg>WWW.TOZVAR.CH</li>
  </ul>
</section>

<section class="card card--contact-b">
  <div class="brand brand--large">TozVar</div>
  <ul class="contacts">
    <li><svg><use href="#icon-phone"/></svg>+41 (71) 402 55 18</li>
    <li><svg><use href="#icon-mail"/></svg>INFO@TOZVAR.CH</li>
    <li><svg><use href="#icon-web"/></svg>WWW.TOZVAR.CH</li>
  </ul>
  <p class="address-line">WERKHOFWEG 7, 9405 SEEBRUNN, OSTGAU</p>
  <svg class="arrow-panel" viewBox="0 0 72 297" preserveAspectRatio="none" aria-hidden="true">
    <rect width="72" height="297" fill="var(--slate)"/>
    <polygon points="0,0 54,153 0,297" fill="var(--steel)"/>
  </svg>
</section>
</body>
</html>
```